Business Card for boutique psychology business

Business card for boutique psychology practice in Melbourne. I want them to be relatively simply with the logo and backing colour taking up the front side. Then, text on the back, with my name; professional title (Clinical Psychologist); website - torvinpsychology.com.au; email: hello@torvinpsychology.com.au; insta: @torvin.psychology.emdr
Back should also have the words: Connect. Integrate. Evolve
Fonts used for logo are: Mikea Demo and Gotham Medium. Use something for back text that will compliment these.
Brand colours uploaded below. I'd like to see options in both olive and blush.

```html
<!DOCTYPE html>
<html lang="en">
<head>
<meta charset="UTF-8">
<title>Torvin Psychology – Business Card</title>
<link rel="stylesheet" href="https://fonts.googleapis.com/css2?family=Josefin+Sans:wght@300&family=Montserrat:wght@500;600&display=swap">
<style>
  :root {
    --stage: #2b2a27;
    --blush-light: #f2ded0;
    --blush-deep: #e1bfa9;
    --olive: #3e4a2b;
    --olive-deep: #343f24;
    --ink: #3b4526;
    --cream: #ecdcc8;
    --gold: rgba(214, 178, 140, 0.35);
    --olive-line: rgba(120, 135, 90, 0.35);
  }
  * { margin: 0; padding: 0; box-sizing: border-box; }
  html, body { width: 1200px; height: 901px; overflow: hidden; background: var(--stage); }
  .canvas {
    position: relative; width: 1200px; height: 901px;
    display: flex; align-items: center; justify-content: center; gap: 60px;
  }
  .card {
    position: relative; width: 520px; height: 310px; border-radius: 22px; overflow: hidden;
    box-shadow: 0 14px 30px rgba(0,0,0,0.45);
  }
  .card--blush { background: linear-gradient(135deg, var(--blush-light), var(--blush-deep)); color: var(--ink); }
  .card--olive { background: linear-gradient(135deg, var(--olive), var(--olive-deep)); color: var(--cream); }

  .corner-motif { position: absolute; width: 130px; height: 120px; }
  .card--blush .corner-motif { background: radial-gradient(circle at 50% 50%, var(--gold), transparent 70%); }
  .card--olive .corner-motif { background: radial-gradient(circle at 50% 50%, var(--olive-line), transparent 70%); }
  .corner-motif--tl { top: -20px; left: -20px; }
  .corner-motif--br { bottom: -20px; right: -20px; }

  .brand {
    position: absolute; left: 44px; bottom: 58px;
    display: flex; align-items: center; gap: 10px;
    font-family: "Montserrat", sans-serif; font-weight: 500; font-size: 52px;
    color: var(--ink); letter-spacing: -1px;
  }
  .brand__dot { width: 10px; height: 10px; border-radius: 50%; background: var(--ink); }

  .details { position: absolute; left: 262px; top: 46px; }
  .details__name {
    font-family: "Josefin Sans", sans-serif; font-weight: 300; font-size: 27px; letter-spacing: 1.5px;
  }
  .details__title {
    font-family: "Montserrat", sans-serif; font-weight: 600; font-size: 13px; margin: 4px 0 0 10px;
  }
  .details__divider { width: 8px; height: 8px; border-radius: 50%; background: var(--ink); margin: 14px 0 14px 24px; }
  .contact { list-style: none; margin-left: 16px; }
  .contact__item {
    display: flex; align-items: center; gap: 9px;
    font-family: "Montserrat", sans-serif; font-weight: 600; font-size: 12.5px; line-height: 21px;
  }
  .contact__icon { width: 13px; height: 13px; flex: none; }

  .tagline {
    position: absolute; inset: 0; display: flex; align-items: center; justify-content: center; gap: 16px;
    font-family: "Josefin Sans", sans-serif; font-weight: 300; font-size: 30px; letter-spacing: 1.5px;
  }
  .tagline__sep { width: 6px; height: 6px; border-radius: 50%; background: var(--cream); }
</style>
</head>
<body>
<main class="canvas">
  <section class="card card--blush" aria-label="Card front, blush">
    <div class="corner-motif corner-motif--tl" role="img" aria-label="Soft leaf-line corner pattern"></div>
    <div class="corner-motif corner-motif--br" role="img" aria-label="Soft leaf-line corner pattern"></div>

    <div class="brand"><span class="brand__name">torvin</span><span class="brand__dot"></span></div>

    <div class="details">
      <p class="details__name">Daniel Harrow</p>
      <p class="details__title">Clinical Psychologist</p>
      <div class="details__divider"></div>
      <ul class="contact">
        <li class="contact__item">
          <svg class="contact__icon" viewBox="0 0 16 16"><path d="M3 1.5l3 .5 1 3.5-2 1.2a9 9 0 0 0 4.3 4.3l1.2-2 3.5 1 .5 3c-.3.8-1 1.2-2 1.2C6.5 14.2 1.8 9.5 1.8 3.5c0-1 .4-1.7 1.2-2z" fill="currentColor"/></svg>
          0400 123 456
        </li>
        <li class="contact__item">
          <svg class="contact__icon" viewBox="0 0 16 16"><rect x="1.5" y="3.5" width="13" height="9" fill="none" stroke="currentColor" stroke-width="1.4"/><path d="M1.5 3.5l6.5 5 6.5-5" fill="none" stroke="currentColor" stroke-width="1.4"/></svg>
          hello@torvinpsychology.com.au
        </li>
        <li class="contact__item">
          <svg class="contact__icon" viewBox="0 0 16 16"><circle cx="8" cy="8" r="6.3" fill="none" stroke="currentColor" stroke-width="1.4"/><ellipse cx="8" cy="8" rx="2.6" ry="6.3" fill="none" stroke="currentColor" stroke-width="1.2"/><path d="M1.7 8h12.6" stroke="currentColor" stroke-width="1.2"/></svg>
          torvinpsychology.com.au
        </li>
        <li class="contact__item">
          <svg class="contact__icon" viewBox="0 0 16 16"><circle cx="8" cy="8" r="3.5" fill="currentColor"/></svg>
          @torvin.psychology.emdr
        </li>
      </ul>
    </div>
  </section>

  <section class="card card--olive" aria-label="Card back, olive">
    <div class="corner-motif corner-motif--tl" role="img" aria-label="Soft leaf-line corner pattern"></div>
    <div class="corner-motif corner-motif--br" role="img" aria-label="Soft leaf-line corner pattern"></div>
    <p class="tagline">
      <span>Connect</span><span class="tagline__sep"></span>
      <span>Integrate</span><span class="tagline__sep"></span>
      <span>Evolve</span>
    </p>
  </section>
</main>
</body>
</html>
```